Boutique Financial Services/Advisor Business Needs Web Design

Looking for an informational and functional web design for my Financial Services/Financial Advisement business. It should have functionality for Company name, address, phone #, "About Us", Who we are, Our Mission, Services we offer, Biographies/Photos of/about "The Team", and possibly a link to "Contact Us". Would like to see something new & exciting blended with a traditional/professional look that will appeal to those approaching retirement, as well as those younger clients that are beginning to think about planning for the future. I already have a web domain through HostMeadow, but would like this to be the design we use for that domain.
Financial Services/Financial Advisor
Coded - Design and coding required
1 page

```html
<!DOCTYPE html>
<html lang="en">
<head>
<meta charset="utf-8">
<title>Meridian Peak Wealth Management</title>
<link rel="stylesheet" href="https://fonts.googleapis.com/css2?family=Cinzel:wght@500;600&family=Jost:wght@400;500;600&display=swap">
<style>
:root{
  --blue:#0b6fc0;
  --blue-deep:#0758a3;
  --navy:#0a0f5c;
  --ink:#1c1c2a;
  --muted:#6d6f78;
  --pale:#e7eff8;
  --circle:#e3edf7;
  --card-grey:#e9e9e9;
  --footer:#141414;
  --white:#ffffff;
}
*{box-sizing:border-box;margin:0;padding:0}
html,body{width:1200px;height:4132px;overflow:hidden}
body{font-family:"Jost",sans-serif;color:var(--ink);background:var(--white);position:relative}
section,header,footer{position:absolute;left:0;width:1200px;overflow:hidden}
.ph{position:absolute}
.btn{position:absolute;background:var(--navy);color:var(--white);border-radius:20px;font-size:15px;font-weight:500;display:flex;align-items:center;justify-content:center;letter-spacing:.3px}
.section-title{position:absolute;left:0;width:1200px;text-align:center;font-family:"Cinzel",serif;font-weight:500;color:var(--blue);font-size:44px;letter-spacing:1px}
.arrows{position:absolute;display:flex;gap:12px}
.arrows span{width:37px;height:37px;border-radius:50%;background:var(--white);display:flex;align-items:center;justify-content:center;box-shadow:0 0 0 1px #d9e2ec}

/* header */
.site-header{top:0;height:112px;background:var(--white)}
.brand{position:absolute;left:64px;top:30px;display:flex;align-items:center;gap:10px;color:var(--navy);font-family:"Cinzel",serif;font-weight:500;font-size:16px;line-height:1.15}
.brand-mark{width:22px;height:22px;background:var(--navy)}
.nav{position:absolute;right:64px;top:48px;display:flex;align-items:center;gap:38px;font-size:15px;font-weight:500;color:var(--ink)}
.nav .active{color:var(--blue)}
.nav .pill{background:var(--blue);color:var(--white);padding:6px 14px;border-radius:16px}

/* hero */
.hero{top:112px;height:430px;background:linear-gradient(90deg,#0865b4 0%,#0b6fc0 55%,#1f83d1 100%)}
.hero h1{position:absolute;left:64px;top:70px;font-family:"Cinzel",serif;font-weight:500;color:var(--white);font-size:47px;line-height:75px;letter-spacing:1px}
.hero p{position:absolute;left:64px;top:228px;width:560px;color:var(--white);font-size:13px;line-height:16.5px}
.hero .btn{left:64px;top:318px;width:246px;height:36px}
.hero-photo{left:760px;top:0;width:230px;height:430px;background:linear-gradient(180deg,#4b6a8c 0%,#1c2430 60%,#20283a 100%)}
.play{position:absolute;left:742px;top:238px;width:76px;height:76px;border-radius:50%;background:var(--white)}
.badge{position:absolute;left:966px;top:313px;width:148px;height:84px;background:var(--white);border-radius:10px;text-align:center;color:var(--blue)}
.badge b{display:block;font-size:31px;font-weight:600;margin-top:8px}
.badge small{font-size:11px;font-weight:600;letter-spacing:.4px}
.dot{position:absolute;width:9px;height:9px;border-radius:50%;background:var(--white)}

/* about */
.about{top:542px;height:619px}
.about h2{position:absolute;left:669px;top:88px;font-family:"Cinzel",serif;font-weight:500;color:var(--blue);font-size:44px;letter-spacing:1px}
.about .copy{position:absolute;left:669px;top:158px;width:470px;font-size:13.2px;line-height:16.5px;color:var(--ink)}
.about .copy p{margin-bottom:16px}
.about .btn{left:669px;top:494px;width:120px;height:36px}

/* services */
.services{top:1161px;height:1024px;background:var(--pale)}
.services .section-title{top:26px}
.svc-card{position:absolute;width:348px;height:422px;background:var(--white);text-align:center}
.svc-icon{position:absolute;left:118px;top:56px;width:112px;height:112px;border-radius:50%;background:var(--circle);display:flex;align-items:center;justify-content:center}
.svc-card h3{position:absolute;left:0;width:348px;top:204px;color:var(--blue);font-size:20px;font-weight:600;letter-spacing:.3px}
.svc-card p{position:absolute;left:26px;width:296px;top:252px;font-size:13px;line-height:16.5px;color:var(--muted)}
.svc-card .btn{left:40px;top:350px;width:268px;height:36px;justify-content:space-between;padding:0 34px}

/* team */
.team{top:2185px;height:521px}
.team .section-title{top:46px;color:var(--blue)}
.member{position:absolute;top:215px;width:248px;height:242px;background:var(--card-grey);text-align:center}
.member.featured{background:var(--blue);color:var(--white)}
.avatar{position:absolute;left:52px;top:-50px;width:144px;height:144px;border-radius:50%;background:linear-gradient(180deg,#c9cfd6,#8a94a2);border:4px solid var(--white)}
.member h4{position:absolute;left:0;width:248px;top:106px;font-size:20px;font-weight:500}
.member .role{position:absolute;left:0;width:248px;top:140px;font-size:14px;color:var(--muted)}
.member.featured .role{color:var(--white)}
.socials{position:absolute;left:0;width:248px;top:188px;display:flex;justify-content:center;gap:16px}
.socials span{width:28px;height:28px;border-radius:50%;background:var(--white);box-shadow:0 0 0 1px #d6d6d6}

/* contact */
.contact{top:2706px;height:486px;background:linear-gradient(90deg,#1d2026 0%,#2d2f36 40%,#3a3432 62%,#24262b 100%)}
.contact-photo{left:230px;top:0;width:380px;height:486px;background:linear-gradient(180deg,#3a3330,#6b4a40 70%,#8a3a34)}
.contact h2{position:absolute;left:64px;top:66px;font-family:"Cinzel",serif;font-weight:500;color:var(--white);font-size:42px}
.contact .sub{position:absolute;left:64px;top:124px;color:var(--white);font-size:14px;font-weight:500}
.c-item{position:absolute;left:62px;display:flex;align-items:center;gap:24px;color:var(--white);font-size:15px;font-weight:500}
.c-icon{width:44px;height:44px;border-radius:50%;background:var(--white);display:flex;align-items:center;justify-content:center}
.form-title{position:absolute;left:601px;width:535px;text-align:center;top:66px;font-family:"Cinzel",serif;font-weight:500;color:var(--white);font-size:42px}
.form-sub{position:absolute;left:601px;width:535px;text-align:center;top:124px;color:var(--white);font-size:14px;font-weight:500}
.field{position:absolute;background:var(--white);font-size:12px;color:#8a8a8a;padding:10px 16px}
.send{position:absolute;left:601px;top:391px;width:535px;height:34px;background:var(--navy);color:var(--white);font-size:15px;font-weight:500;display:flex;align-items:center;justify-content:center}

/* news */
.news{top:3192px;height:602px;background:var(--pale)}
.news .section-title{top:38px}
.post{position:absolute;top:135px;width:345px}
.post .img{height:213px;position:relative}
.post .meta{display:flex;justify-content:space-between;font-size:11px;color:var(--blue);margin:24px 6px 0}
.post h5{font-size:16px;font-weight:500;margin:16px 6px 0}
.post p{font-size:13px;line-height:16.5px;margin:14px 6px 0;width:300px}
.post .btn{position:absolute;left:2px;top:378px;width:136px;height:36px}

/* footer */
.site-footer{top:3794px;height:338px;background:var(--footer);color:var(--white)}
.f-brand{position:absolute;left:64px;top:100px;display:flex;align-items:center;gap:12px;font-family:"Cinzel",serif;font-weight:500;font-size:20px;line-height:1.15;color:var(--white)}
.f-brand-mark{width:26px;height:26px;background:var(--white)}
.f-about{position:absolute;left:64px;top:185px;width:260px;font-size:13px;line-height:16.5px}
.f-col{position:absolute;top:66px}
.f-col h6{font-family:"Cinzel",serif;font-weight:500;color:var(--blue);font-size:17px;margin-bottom:14px}
.f-col li{list-style:none;font-size:13px;line-height:26px;display:flex;align-items:center;gap:10px}
.f-col li::before{content:"";width:6px;height:6px;background:var(--blue);transform:rotate(45deg)}
.f-rule{position:absolute;left:0;top:280px;width:1200px;height:1px;background:#3a3a3a}
.copyright{position:absolute;left:0;width:1200px;top:303px;text-align:center;font-size:13px}
</style>
</head>
<body>

<header class="site-header">
  <div class="brand"><span class="brand-mark"></span><span>MERIDIAN PEAK<br>WEALTH MANAGEMENT</span></div>
  <nav class="nav">
    <span class="active">HOME</span><span>ABOUT US</span><span>SERVICES</span><span>OUR TEAM</span><span class="pill">CONTACT US</span>
  </nav>
</header>

<section class="hero">
  <div class="ph hero-photo" role="img" aria-label="Portrait of a smiling financial advisor holding a folder"></div>
  <h1>YOUR FINANCIAL<br>FUTURE, SECURED</h1>
  <p>We are a full-service financial practice committed to helping people pursue their financial goals. We offer a wide range of financial products and services to individuals and business owners. We believe you will be better able to identify your goals and make sound decisions to help reach them by our providing sound financial information.</p>
  <div class="btn">SCHEDULE A CONSULTATION</div>
  <div class="play">
    <svg width="76" height="76" viewBox="0 0 76 76"><path d="M32 26 L52 38 L32 50 Z" fill="#0b6fc0"/></svg>
  </div>
  <div class="badge"><b>20+</b><small>YEARS EXPERIENCE</small></div>
  <span class="dot" style="left:598px;top:71px"></span>
  <span class="dot" style="left:768px;top:98px;width:6px;height:6px"></span>
  <span class="dot" style="left:1155px;top:50px"></span>
</section>

<section class="about">
  <div class="ph" style="left:61px;top:72px;width:263px;height:244px;background:linear-gradient(135deg,#cfd6d6,#8b9aa0)" role="img" aria-label="Senior couple saving coins in a piggy bank"></div>
  <div class="ph" style="left:335px;top:72px;width:265px;height:244px;background:linear-gradient(135deg,#4e5a62,#c9c6c0)" role="img" aria-label="Woman reviewing financial papers at a laptop"></div>
  <div class="ph" style="left:59px;top:326px;width:541px;height:225px;background:linear-gradient(135deg,#6f7b85,#b8b2a8 60%,#d8d2c6)" role="img" aria-label="Advisor shaking hands with a couple in an office"></div>
  <h2>ABOUT US</h2>
  <div class="copy">
    <p>We are a full-service financial practice committed to helping people pursue their financial goals. We offer a wide range of financial products and services to individuals and business owners. We believe you will be better able to identify your goals and make sound decisions to help reach them by our providing sound financial information.</p>
    <p>We are committed to maintaining the highest standards of integrity and professionalism in our relationship with you, our client. We endeavor to know and understand your financial situation and provide you with only the highest quality information, services, and products to help you reach your goals.</p>
    <p>We're here to help educate you about the basic concepts of financial management; to help you learn more about who we are; and to give you fast, easy access to market performance data.</p>
    <p>We hope you take advantage of this resource and visit us often. Be sure to add our site to your list of "favorites" in your Internet browser. We frequently update our information, and we wouldn't want you to miss any developments in the area of personal finance.</p>
  </div>
  <div class="btn">READ MORE</div>
</section>

<section class="services">
  <h2 class="section-title">SERVICES</h2>
  <div class="arrows" style="left:1049px;top:33px">
    <span><svg width="18" height="10"><path d="M17 5H2M6 1L2 5l4 4" stroke="#1c1c2a" fill="none" stroke-width="1.5"/></svg></span>
    <span><svg width="18" height="10"><path d="M1 5h15M12 1l4 4-4 4" stroke="#1c1c2a" fill="none" stroke-width="1.5"/></svg></span>
  </div>

  <div class="svc-card" style="left:63px;top:101px">
    <div class="svc-icon"><svg width="44" height="44" viewBox="0 0 44 44" fill="none" stroke="#0b6fc0" stroke-width="1.6"><rect x="12" y="6" width="22" height="16" rx="2"/><circle cx="23" cy="14" r="4"/><path d="M4 30h8l8 4h10l8-6M4 38h10"/></svg></div>
    <h3>WEALTH MANAGEMENT</h3>
    <p>Lorem ipsum dolor sit amet, consectetuer adipiscing elit, sed diam nonummy nibh euismod tincidunt ut laoreet dolore magna aliquam erat volutpat. Ut wisi enim ad minim ...</p>
    <div class="btn"><span>READ MORE</span><span>→</span></div>
  </div>
  <div class="svc-card" style="left:427px;top:101px">
    <div class="svc-icon"><svg width="44" height="44" viewBox="0 0 44 44" fill="none" stroke="#0b6fc0" stroke-width="1.6"><rect x="8" y="6" width="22" height="30" rx="2"/><path d="M13 14h12M13 20h12M13 26h8"/><circle cx="32" cy="32" r="7"/></svg></div>
    <h3>RETIREMENT PLANS</h3>
    <p>Lorem ipsum dolor sit amet, consectetuer adipiscing elit, sed diam nonummy nibh euismod tincidunt ut laoreet dolore magna aliquam erat volutpat. Ut wisi enim ad minim ...</p>
    <div class="btn"><span>READ MORE</span><span>→</span></div>
  </div>
  <div class="svc-card" style="left:789px;top:101px">
    <div class="svc-icon"><svg width="44" height="44" viewBox="0 0 44 44" fill="none" stroke="#0b6fc0" stroke-width="1.6"><path d="M18 8h8l-2 5h-4z"/><path d="M16 14c-6 5-6 14 6 14s12-9 6-14z"/><path d="M4 34h10l6 3h12l8-5"/></svg></div>
    <h3>TAX PLANNING</h3>
    <p>Lorem ipsum dolor sit amet, consectetuer adipiscing elit, sed diam nonummy nibh euismod tincidunt ut laoreet dolore magna aliquam erat volutpat. Ut wisi enim ad minim ...</p>
    <div class="btn"><span>READ MORE</span><span>→</span></div>
  </div>
  <div class="svc-card" style="left:63px;top:538px">
    <div class="svc-icon"><svg width="44" height="44" viewBox="0 0 44 44" fill="none" stroke="#0b6fc0" stroke-width="1.6"><path d="M6 38h32"/><rect x="9" y="24" width="5" height="14"/><rect x="18" y="18" width="5" height="20"/><rect x="27" y="26" width="5" height="12"/><circle cx="14" cy="10" r="5"/></svg></div>
    <h3>EXECUTIVE COMPENSATION</h3>
    <p>Lorem ipsum dolor sit amet, consectetuer adipiscing elit, sed diam nonummy nibh euismod tincidunt ut laoreet dolore magna aliquam erat volutpat. Ut wisi enim ad minim ...</p>
    <div class="btn"><span>READ MORE</span><span>→</span></div>
  </div>
  <div class="svc-card" style="left:427px;top:538px">
    <div class="svc-icon"><svg width="44" height="44" viewBox="0 0 44 44" fill="none" stroke="#0b6fc0" stroke-width="1.6"><circle cx="24" cy="14" r="7"/><path d="M12 38c0-8 5-13 12-13s12 5 12 13"/><circle cx="12" cy="30" r="6"/></svg></div>
    <h3>EMPLOYEE BENEFITS</h3>
    <p>Lorem ipsum dolor sit amet, consectetuer adipiscing elit, sed diam nonummy nibh euismod tincidunt ut laoreet dolore magna aliquam erat volutpat. Ut wisi enim ad minim ...</p>
    <div class="btn"><span>READ MORE</span><span>→</span></div>
  </div>
  <div class="svc-card" style="left:789px;top:538px">
    <div class="svc-icon"><svg width="44" height="44" viewBox="0 0 44 44" fill="none" stroke="#0b6fc0" stroke-width="1.6"><rect x="10" y="6" width="24" height="32" rx="2"/><path d="M22 14h8M22 22h8M16 30h14"/><circle cx="15" cy="18" r="4"/></svg></div>
    <h3>FINANCIAL PLANNING</h3>
    <p>Lorem ipsum dolor sit amet, consectetuer adipiscing elit, sed diam nonummy nibh euismod tincidunt ut laoreet dolore magna aliquam erat volutpat. Ut wisi enim ad minim ...</p>
    <div class="btn"><span>READ MORE</span><span>→</span></div>
  </div>
</section>

<section class="team">
  <h2 class="section-title">OUR TEAM</h2>
  <div class="arrows" style="left:1049px;top:54px">
    <span><svg width="18" height="10"><path d="M17 5H2M6 1L2 5l4 4" stroke="#0b6fc0" fill="none" stroke-width="1.5"/></svg></span>
    <span><svg width="18" height="10"><path d="M1 5h15M12 1l4 4-4 4" stroke="#1c1c2a" fill="none" stroke-width="1.5"/></svg></span>
  </div>
  <div class="member featured" style="left:63px">
    <div class="avatar" role="img" aria-label="Portrait of Owen"></div>
    <h4>Owen</h4><div class="role">Chief Financial Officer</div>
    <div class="socials"><span></span><span></span><span></span></div>
  </div>
  <div class="member" style="left:337px">
    <div class="avatar" role="img" aria-label="Portrait of Marisol"></div>
    <h4>Marisol</h4><div class="role">Country Manager</div>
    <div class="socials"><span></span><span></span><span></span></div>
  </div>
  <div class="member" style="left:614px">
    <div class="avatar" role="img" aria-label="Portrait of Theodore"></div>
    <h4>Theodore</h4><div class="role">Chief Financial Officer</div>
    <div class="socials"><span></span><span></span><span></span></div>
  </div>
  <div class="member" style="left:884px">
    <div class="avatar" role="img" aria-label="Portrait of Clara"></div>
    <h4>Clara</h4><div class="role">Country Manager</div>
    <div class="socials"><span></span><span></span><span></span></div>
  </div>
</section>

<section class="contact">
  <div class="ph contact-photo" role="img" aria-label="Woman working on a laptop in a dim office"></div>
  <h2>CONTACT</h2>
  <div class="sub">Meridian Peak Wealth Management</div>
  <div class="c-item" style="top:175px"><span class="c-icon"><svg width="20" height="20" viewBox="0 0 20 20"><path d="M4 2l4 1 1 4-2 2c1 2 3 4 5 5l2-2 4 1 0 4c-9 0-16-7-14-15z" fill="#0b6fc0"/></svg></span>555-014-2290</div>
  <div class="c-item" style="top:247px"><span class="c-icon"><svg width="20" height="20" viewBox="0 0 20 20"><path d="M10 1a6 6 0 0 0-6 6c0 5 6 12 6 12s6-7 6-12a6 6 0 0 0-6-6z" fill="#0b6fc0"/><circle cx="10" cy="7" r="2.3" fill="#fff"/></svg></span>1140 Harbor Lane, Suite 210 Fairview, OH</div>
  <div class="c-item" style="top:318px"><span class="c-icon"><svg width="22" height="22" viewBox="0 0 22 22" fill="none" stroke="#0b6fc0" stroke-width="1.6"><circle cx="11" cy="11" r="9"/><ellipse cx="11" cy="11" rx="4" ry="9"/><path d="M2 11h18"/></svg></span>www.meridianpeakwealth.com</div>
  <div class="c-item" style="top:390px"><span class="c-icon"><svg width="20" height="20" viewBox="0 0 20 20" fill="#0b6fc0"><rect x="5" y="2" width="10" height="5"/><rect x="2" y="8" width="16" height="7" rx="1"/><rect x="5" y="13" width="10" height="5" fill="#fff" stroke="#0b6fc0"/></svg></span>555-014-2290</div>

  <div class="form-title">MESSAGE US</div>
  <div class="form-sub">Please complete the Contact Form and we'll be in touch</div>
  <div class="field" style="left:601px;top:159px;width:535px;height:36px">Your Name</div>
  <div class="field" style="left:601px;top:210px;width:260px;height:36px">Phone .No</div>
  <div class="field" style="left:876px;top:210px;width:260px;height:36px">E - Mail</div>
  <div class="field" style="left:601px;top:261px;width:535px;height:113px">Message...</div>
  <div class="send">SEND MESSAGE</div>
</section>

<section class="news">
  <h2 class="section-title">LATEST NEWS</h2>
  <div class="arrows" style="left:1049px;top:50px">
    <span><svg width="18" height="10"><path d="M17 5H2M6 1L2 5l4 4" stroke="#1c1c2a" fill="none" stroke-width="1.5"/></svg></span>
    <span><svg width="18" height="10"><path d="M1 5h15M12 1l4 4-4 4" stroke="#1c1c2a" fill="none" stroke-width="1.5"/></svg></span>
  </div>
  <article class="post" style="left:64px">
    <div class="img" style="background:linear-gradient(135deg,#6b4a32,#c9b79c 60%,#e4dccd)" role="img" aria-label="Desk with laptop and a notebook sketch about finance"></div>
    <div class="meta"><span>11 Mar 2024</span><span>Read 7 Mins</span></div>
    <h5>Eight Great Investing Quotes</h5>
    <p>Lorem ipsum dolor sit amet, consectetuer adipiscing elit, sed diam nonummy nibh euismod tincidunt ut laoreet dolore magna ...</p>
    <div class="btn">READ MORE</div>
  </article>
  <article class="post" style="left:427px">
    <div class="img" style="background:linear-gradient(135deg,#3d4a3a,#a9a59b 55%,#2b3444)" role="img" aria-label="Advisor meeting with a couple at a table"></div>
    <div class="meta"><span>23 Jan 2017</span><span>Read 7 Mins</span></div>
    <h5>Do You Have Enough Life Insurance?</h5>
    <p>Lorem ipsum dolor sit amet, consectetuer adipiscing elit, sed diam nonummy nibh euismod tincidunt ut laoreet dolore magna ...</p>
    <div class="btn">READ MORE</div>
  </article>
  <article class="post" style="left:791px">
    <div class="img" style="background:linear-gradient(135deg,#e8e4dc,#b7b2a8 50%,#e9c25a)" role="img" aria-label="Calculator, coins, magnifier and piggy bank on financial papers"></div>
    <div class="meta"><span>30 Mar 2024</span><span>Read 7 Mins</span></div>
    <h5>Key Retirement and Tax Numbers for 2024</h5>
    <p>Lorem ipsum dolor sit amet, consectetuer adipiscing elit, sed diam nonummy nibh euismod tincidunt ut laoreet dolore magna ...</p>
    <div class="btn">READ MORE</div>
  </article>
</section>

<footer class="site-footer">
  <div class="f-brand"><span class="f-brand-mark"></span><span>MERIDIAN PEAK<br>WEALTH MANAGEMENT</span></div>
  <p class="f-about">We are a full-service financial practice committed to helping people pursue their financial goals</p>
  <div class="f-col" style="left:585px">
    <h6>QUICK LINKS</h6>
    <ul><li>Home</li><li>About Us</li><li>Services</li><li>Our Team</li><li>Contact Us</li></ul>
  </div>
  <div class="f-col" style="left:975px">
    <h6>SERVICES</h6>
    <ul><li>Estate Planning</li><li>Retirement Planning</li><li>Financial Planning</li><li>Wealth Management</li><li>Employee Benefits</li></ul>
  </div>
  <div class="f-rule"></div>
  <div class="copyright">© Copyright 2024 All Rights Reserved</div>
</footer>

</body>
</html>
```